Morivane Sports K.K. PPT Design (Sales Presentation Template)

We need a PPT design for our new e-commerce sports apparel business that we are launching next month. We have a base design that was used to create our investor pitch deck. I am looking for something that our sales apparatus can use when getting new business. Our clients are professional sports teams. At the moment, our clients are all baseball teams. I would like the deck to use the colors of each baseball team that we present to. For example, The Tobrenn Herons colors are red and blue. I would want the deck to be done in those colors. Our corporate or base colors are yellow and black. Do you you get where I am going with this?

Target Market(s)

professional sports teams. currently Japanese baseball teams.

Industry/Entity Type

Business

Requirements
Must have
• 1. base black and yellow corporate colors as well as our logo
• 2. 12 different variations for the 12 baseball teams here in Japan:
• 1. Valdeno Titans
• 2. Quorvel Ravens
• 3. Tobrenn Herons
• 4. Belcastro Pike
• 5. Ferul Pumas
• 6. Pelto Grivan Sailors
• 7. Sandrevo QuLix
• 8. Orvane Malt Strikers
• 9. Zemparo Condors
• 10. Velmora Jaguars
• 11. Tavu Bisonettes
• 12. Plenvoa Griffins
Nice to have
• http://trelvanatlas.example/wp-content/uploads/2012/03/league_chart_2012_v.gif

```html
<!DOCTYPE html>
<html lang="en">
<head>
<meta charset="utf-8">
<title>Morivane Sports K.K. — Sales Slide Template</title>
<link rel="stylesheet" href="https://fonts.googleapis.com/css2?family=Roboto+Condensed:wght@700&display=swap">
<style>
  :root {
    --slide-bg: #ffffff;
    --brand-black: #000000;
    --brand-yellow: #f5c518;
    --team-text: #111111;
  }
  html, body {
    margin: 0;
    padding: 0;
    width: 1200px;
    height: 718px;
    overflow: hidden;
    background: var(--slide-bg);
  }
  .slide {
    position: relative;
    width: 1200px;
    height: 718px;
    background: var(--slide-bg);
    overflow: hidden;
  }
  .slide__wave {
    position: absolute;
    left: 0;
    top: 0;
    width: 1200px;
    height: 718px;
    display: block;
  }
  .wave__line { fill: var(--brand-black); }
  .wave__band { fill: var(--brand-yellow); }
  .wave__base { fill: var(--brand-black); }
  .team-name {
    position: absolute;
    left: 924px;
    top: 560px;
    width: 206px;
    margin: 0;
    text-align: center;
    font-family: "Roboto Condensed", sans-serif;
    font-weight: 700;
    font-size: 26px;
    line-height: 1;
    letter-spacing: 0.5px;
    color: var(--team-text);
  }
</style>
</head>
<body>
  <main class="slide">
    <svg class="slide__wave" viewBox="0 0 1200 718" aria-hidden="true">
      <path class="wave__line" d="M0,609 C300,652 700,642 1200,586 L1200,718 L0,718 Z"/>
      <path class="wave__band" d="M0,616 C300,659 700,649 1200,592 L1200,718 L0,718 Z"/>
      <path class="wave__base" d="M0,645 C260,688 660,678 1200,612 L1200,718 L0,718 Z"/>
    </svg>
    <p class="team-name">Quorvel Ravens</p>
  </main>
</body>
</html>
```